Steel Company / Iron Railing Business Card Template

We are a custom steel fabrication company located in Harwell, DE. In business since 1979, we recently developed a new logo, and we're looking for a business card design to help display the new logo and our business. The name of the company is Kelbrook Forge Co.. The Office Phone number is (610) 555-0143. We fabricate and install custom "wrought iron" railings on our residential side, we also fabricate and erect structural steel (think cranes and steel beams in buildings) on our commercial side. Looking to get a business card template designed. Something modern, but professional. Clear and easy to read. Front should have all business and employee information including phone number(s), email address, business information, etc. back should spotlight logo.

Industry/Entity Type

Construction / Home Improvement

Contact Information for Business Card

Business information is Kelbrook Forge Co., 48 Dunmore Ave Suite 3305, Harwell, DE 19074. Phone number is (610) 555-0143. Website is www.kelbrookforge.example Business card should be for "Tom Pelling" with the job title "Sales & Estimating" but be editable for other employees. Tom's phone number is (610) 555-0178

Colors

Designer to choose colors to be used in the design.

Requirements
Must have
• Modern Feel, Design should be sized for standard business card sizing 3.5" x 2" (88.9mm x 50.8mm)

```html
<!DOCTYPE html>
<html lang="en">
<head>
<meta charset="utf-8">
<title>Kelbrook Forge Co. – Business Card</title>
<link rel="stylesheet" href="https://fonts.googleapis.com/css2?family=Montserrat:wght@400;500;700&display=swap">
<style>
  :root {
    --ground: #e4e4e2;
    --navy: #243f86;
    --red: #c8262f;
    --white: #ffffff;
    --paper: #f6f6f4;
  }
  * { margin: 0; padding: 0; box-sizing: border-box; }
  html, body { width: 1200px; height: 801px; overflow: hidden; }
  body {
    background: var(--ground);
    font-family: "Montserrat", Arial, sans-serif;
    position: relative;
  }
  .card {
    position: absolute;
    top: 243px;
    width: 550px;
    height: 314px;
    overflow: hidden;
    box-shadow: 0 6px 18px rgba(0,0,0,0.18);
  }
  .card-front { left: 30px; background: var(--navy); }
  .card-back  { left: 620px; background: var(--navy); }

  .front-shape { position: absolute; inset: 0; }

  .contact {
    position: absolute;
    left: 32px;
    top: 92px;
    color: var(--white);
    font-size: 13px;
    line-height: 1.45;
    font-weight: 400;
  }
  .contact .name { color: var(--red); font-size: 21px; font-weight: 500; line-height: 1.15; }
  .contact .title { font-size: 14px; }
  .contact .group { margin-top: 14px; }
  .line { display: flex; align-items: center; gap: 7px; }
  .icon { width: 14px; height: 14px; flex: none; }

  .wordmark {
    position: absolute;
    color: var(--navy);
    font-weight: 700;
    font-size: 27px;
    line-height: 1.1;
    text-align: center;
    letter-spacing: 0.5px;
  }
  .card-front .wordmark { right: 38px; top: 48px; width: 230px; }
  .card-back .wordmark {
    color: var(--white);
    font-size: 38px;
    left: 0; right: 0; top: 50%;
    transform: translateY(-50%);
  }
</style>
</head>
<body>
  <section class="card card-front" aria-label="Business card front">
    <svg class="front-shape" viewBox="0 0 550 314" width="550" height="314" aria-hidden="true">
      <path d="M205,0 C235,185 385,278 550,290 L550,0 Z" fill="var(--red)"/>
      <path d="M221,0 C252,175 390,262 550,272 L550,0 Z" fill="var(--white)"/>
      <path d="M238,0 C268,165 395,250 550,258 L550,0 Z" fill="var(--red)"/>
      <path d="M248,0 C278,160 400,240 550,246 L550,0 Z" fill="var(--paper)"/>
    </svg>

    <div class="wordmark">Kelbrook<br>Forge Co.</div>

    <div class="contact">
      <div class="name">Tom Pelling</div>
      <div class="title">Sales &amp; Estimating</div>
      <div class="line">
        <svg class="icon" viewBox="0 0 14 14"><circle cx="7" cy="7" r="7" fill="var(--red)"/><path d="M4.3 3.5h1.6l.7 1.8-.9.7a5 5 0 0 0 2.3 2.3l.7-.9 1.8.7v1.6c0 .4-.3.7-.7.7A6.3 6.3 0 0 1 3.6 4.2c0-.4.3-.7.7-.7z" fill="var(--white)"/></svg>
        <span>(610) 555-0178</span>
      </div>

      <div class="group">
        <div>48 Dunmore Ave Suite 3305</div>
        <div>Harwell, DE 19074.</div>
      </div>

      <div class="group">
        <div class="line">
          <svg class="icon" viewBox="0 0 14 14"><circle cx="7" cy="7" r="7" fill="var(--red)"/><path d="M4.3 3.5h1.6l.7 1.8-.9.7a5 5 0 0 0 2.3 2.3l.7-.9 1.8.7v1.6c0 .4-.3.7-.7.7A6.3 6.3 0 0 1 3.6 4.2c0-.4.3-.7.7-.7z" fill="var(--white)"/></svg>
          <span>(610) 555-0143</span>
        </div>
        <div class="line">
          <svg class="icon" viewBox="0 0 14 14"><circle cx="7" cy="7" r="7" fill="var(--red)"/><rect x="3.5" y="4.5" width="7" height="5" fill="none" stroke="var(--white)" stroke-width="1"/><path d="M3.5 4.5 7 7.3l3.5-2.8" fill="none" stroke="var(--white)" stroke-width="1"/></svg>
          <span>info@kelbrookforge.example</span>
        </div>
        <div class="line">
          <svg class="icon" viewBox="0 0 14 14"><circle cx="7" cy="7" r="7" fill="var(--red)"/><circle cx="7" cy="7" r="3.6" fill="none" stroke="var(--white)" stroke-width="1"/><path d="M3.4 7h7.2M7 3.4c-1.6 2-1.6 5.2 0 7.2M7 3.4c1.6 2 1.6 5.2 0 7.2" fill="none" stroke="var(--white)" stroke-width="0.8"/></svg>
          <span>www.kelbrookforge.example</span>
        </div>
      </div>
    </div>
  </section>

  <section class="card card-back" aria-label="Business card back">
    <div class="wordmark">Kelbrook<br>Forge Co.</div>
  </section>
</body>
</html>
```